Web Design Project

We are looking for a new site design for the KELVO Canada. The current site can be found at
http://www.kelvocanada.example/
The URL is provided for reference. We want a completely different look and layout which is shown in the specifications document.
As part of the design, we want a home page, and inside page.
The design you provide will be implemented in Joomla. The design winner will only need to provide the PSD. We anticipate creating the template coding in-house.
However, if you have experience creating Joomla templates, please let us know as we may ask you to bid separately to do that phase of the project.
We've provided a specifications document which includes wireframes of the home page, and inside page. We've also included a logo file.
For the header at the top, as indicated in the specs document, we want to keep the same overall treatment to every page. We want a graphic treatment with the logo for the header area. In this manner, the design will be flexiable and can be used for future years.
For the home page, we've indicated that we'd like to have a slider implemented within the design.
The wireframe is provided to illustrate the placement of content and menu items. The exact dimensions of each component can be revised as you see fit. We are also flexiable if you feel we have missed items.

```html
<!DOCTYPE html>
<html lang="en">
<head>
<meta charset="utf-8">
<title>KELVO Canada</title>
<link href="https://fonts.googleapis.com/css2?family=Ubuntu:wght@400;500;700&display=swap" rel="stylesheet">
<style>
:root{
  --blue:#3a5ba8;
  --blue-dark:#2b4690;
  --blue-light:#4d72cc;
  --red:#d52b2e;
  --red-dark:#b71f22;
  --ink:#333;
  --body:#555;
  --panel:#f4f4f4;
  --border:#d3d3d3;
  --footer:#3b3b3b;
}
*{box-sizing:border-box;margin:0;padding:0}
html,body{width:1112px;height:1200px;overflow:hidden;background:#fff;font-family:"Ubuntu",sans-serif;color:var(--ink)}
.page{position:relative;width:1112px;height:1200px;overflow:hidden}
.topbar{position:absolute;left:0;top:0;width:100%;height:81px;background:linear-gradient(#4a6fca,#2f4b95)}
.utility{position:absolute;top:18px;right:119px;display:flex;gap:9px}
.utility a{display:block;height:26px;line-height:26px;padding:0 11px;background:#5b82dc;color:#fff;font-size:12px;text-decoration:none;border-radius:2px}
.mainnav{position:absolute;left:0;top:81px;width:100%;height:43px;background:linear-gradient(#e0383a,#c52326);border-top:1px solid #f06a6a}
.mainnav ul{position:absolute;left:290px;top:0;display:flex;list-style:none;height:43px;align-items:center}
.mainnav li{color:#fff;font-size:12px;font-weight:500;display:flex;align-items:center}
.mainnav li+li::before{content:"|";margin:0 22px;font-weight:400}
.logo-box{position:absolute;left:120px;top:18px;width:156px;height:135px;background:#fff;border:1px solid #ccc;box-shadow:0 2px 5px rgba(0,0,0,.25);display:flex;align-items:center;justify-content:center;gap:8px;z-index:3}
.logo-box .dot{width:14px;height:14px;border-radius:50%;background:var(--red)}
.logo-box span{font-size:28px;font-weight:700;color:var(--blue-dark)}
.hero{position:absolute;left:0;top:124px;width:100%;height:376px;background:radial-gradient(circle at 40% 50%,#fafafa,#e9e9e9)}
.hero-arc{position:absolute;left:0;top:0}
.hero-copy{position:absolute;left:120px;top:118px;z-index:2}
.hero-copy .kicker{font-size:21px;color:#666}
.hero-copy h1{font-size:37px;font-weight:500;color:#444;line-height:1.1;white-space:nowrap;letter-spacing:-0.3px}
.hero-copy h1 b{color:var(--blue-dark);font-weight:500}
.hero-copy .city{font-size:25px;color:var(--blue-dark);font-weight:500;margin-top:2px}
.hero-copy .date{font-size:29px;color:var(--red);font-weight:500}
.hero-art{position:absolute;left:620px;top:6px;width:350px;height:366px;background:linear-gradient(135deg,#f3f5fa,#dfe5f2);border-radius:4px}
.dots{position:absolute;left:120px;top:328px;display:flex;gap:7px}
.dots i{width:25px;height:25px;border-radius:50%;background:#777}
.dots i:first-child{background:#333}
.box{position:absolute;background:var(--panel);border:1px solid var(--border);box-shadow:0 6px 6px -4px rgba(0,0,0,.2)}
.box-head{height:37px;background:linear-gradient(#4a6fca,#2f4b95);color:#fff;font-size:14px;font-weight:500;padding:0 16px;line-height:38px}
.sponsors{left:120px;top:516px;width:204px;height:162px}
.sponsor-name{text-align:center;font-size:30px;font-weight:700;color:#111;margin-top:20px;letter-spacing:-1px}
.btn-red{display:block;background:var(--red);color:#fff;font-size:14px;font-weight:500;text-align:center;border-radius:2px;text-decoration:none}
.sponsors .btn-red{margin:15px auto 0;width:156px;height:28px;line-height:28px}
.login{left:120px;top:695px;width:204px;height:190px}
.field{display:block;width:174px;height:30px;margin:21px auto 0;border:1px solid #c9c9c9;border-radius:3px;background:#fff;font-size:12px;color:#999;padding-left:11px;line-height:28px}
.field+.field{margin-top:15px}
.login-row{display:flex;justify-content:space-between;align-items:center;padding:17px 14px 0 14px}
.forgot{font-size:11px;color:var(--blue-dark);text-decoration:none}
.login-row .btn-red{width:69px;height:28px;line-height:28px;font-size:14px;color:#fff}
.connect{left:120px;top:902px;width:204px;height:162px}
.social{list-style:none;padding:10px 0 0 13px}
.social li{display:flex;align-items:center;gap:12px;font-size:12px;height:38px}
.social i{width:28px;height:28px;border-radius:3px;background:var(--blue)}
.social li:nth-child(2) i{background:#7cc7e6}
.social li:nth-child(3) i{background:#2a63a8}
.welcome{left:343px;top:516px;width:649px;height:352px;padding:18px 11px 0 11px}
.welcome-head{display:flex;justify-content:space-between;align-items:center}
.welcome h2{font-size:16px;font-weight:500;color:#222}
.news{font-size:13px;color:var(--blue-dark);font-weight:500;margin-right:58px;display:flex;align-items:center;gap:12px}
.news svg{display:block}
.lead{font-size:11.5px;color:var(--red);font-weight:500;line-height:19px;margin-top:12px}
.welcome p.copy{font-size:11.5px;color:var(--body);line-height:21.3px;margin-bottom:6px}
.btn-blue{position:absolute;right:17px;bottom:8px;width:86px;height:26px;line-height:26px;background:var(--blue-dark);color:#fff;font-size:12px;text-align:center;border-radius:2px}
.regions{left:343px;top:883px;width:649px;height:183px;background:#ebebeb;padding:10px 11px}
.regions h2{font-size:16px;font-weight:500;color:#222}
.region-list{display:flex;gap:11px;margin-top:8px}
.region{position:relative;width:148px;height:133px;background:#fff;border:1px solid #c9c9c9;border-radius:4px;padding:10px 11px;overflow:hidden}
.region::before{content:"";position:absolute;left:-60px;top:2px;width:170px;height:170px;border:2px solid #ececec;border-radius:50%}
.region h3{position:relative;font-size:14px;font-weight:500;color:var(--red);line-height:17px}
.region ul{position:relative;list-style:none;margin-top:10px}
.region li{font-size:11px;color:#444;line-height:28px;padding-left:17px;position:relative}
.region li::before{content:"";position:absolute;left:2px;top:11px;width:6px;height:6px;border-radius:50%;background:#e6a94d}
.region.central{padding-top:8px}
.region.central ul{margin-top:3px}
.region.central li{line-height:19px;font-size:10.5px;padding-left:14px;white-space:nowrap}
.region.central li::before{top:7px;left:1px}
.region.atlantic ul{margin-top:8px}
.region.atlantic li{line-height:25px}
.region.atlantic li::before{top:10px}
.footer{position:absolute;left:0;top:1087px;width:100%;height:113px;background:var(--footer);text-align:center;color:#ddd}
.footer-links{font-size:11px;margin-top:40px}
.footer-links span{margin:0 5px;color:#bbb}
.copyright{font-size:11px;color:#fff;font-weight:500;margin-top:10px}
</style>
</head>
<body>
<div class="page">
  <header>
    <div class="topbar">
      <nav class="utility"><a href="#">Home</a><a href="#">Contact Us</a><a href="#">KELVO International</a></nav>
    </div>
    <nav class="mainnav">
      <ul><li>Home</li><li>Boards</li><li>Chapters</li><li>Member Space</li><li>Resources &amp; Knowledge</li><li>Sponsorship</li><li>Exhibit</li></ul>
    </nav>
    <div class="logo-box"><div class="dot"></div><span>KELVO</span></div>
  </header>

  <section class="hero">
    <svg class="hero-arc" width="560" height="376" viewBox="0 0 560 376"><path d="M0 330 C 30 120 220 -10 440 10 C 490 60 520 130 535 200" fill="none" stroke="#e2e2e2" stroke-width="14"/></svg>
    <div class="hero-art" role="img" aria-label="Blue line illustration of a miner swinging a pickaxe beside an ore cart, with the KELVO emblem"></div>
    <div class="hero-copy">
      <div class="kicker">Mining RIM Resources</div>
      <h1><b>KELVO</b> Canada Conference</h1>
      <div class="city">Saskoon, SK</div>
      <div class="date">June 2-5, 2013</div>
    </div>
    <div class="dots"><i></i><i></i><i></i><i></i></div>
  </section>

  <aside>
    <div class="box sponsors">
      <div class="box-head">SPONSORS</div>
      <div class="sponsor-name">NORVANT</div>
      <a class="btn-red" href="#">Become a Sponsor</a>
    </div>
    <div class="box login">
      <div class="box-head">MEMBER LOGIN</div>
      <span class="field">Username</span>
      <span class="field">Password</span>
      <div class="login-row"><a class="forgot" href="#">Forgot Password?</a><a class="btn-red" href="#">Login</a></div>
    </div>
    <div class="box connect">
      <div class="box-head">STAY CONNECTED</div>
      <ul class="social"><li><i></i>Friendspace</li><li><i></i>Chirper</li><li><i></i>ProLink</li></ul>
    </div>
  </aside>

  <main>
    <section class="box welcome">
      <div class="welcome-head">
        <h2>WELCOME TO OUR SITE</h2>
        <div class="news">NEWS &amp; EVENTS <svg width="8" height="14" viewBox="0 0 8 14"><path d="M0 0L8 7L0 14Z" fill="#444"/></svg></div>
      </div>
      <p class="lead">Lorem ipsum dolor sit amet, consectetur adipiscing elit. Fusce accumsan, elit a suscipit sagittis, tortor sapien cursus risus, non rhoncus lectus nunc ac nulla..</p>
      <p class="copy">Aliquam molestie, mi et imperdiet euismod, dui purus auctor tellus, et interdum lacus lectus et ante. Sed accumsan sollicitudin sapien, sit amet adipiscing turpis gravida ac. In congue, neque ac lobortis volutpat, libero mauris varius mi, vitae suscipit ipsum ligula vitae risus. Duis aliquam nibh a dui iaculis viverra id a velit. Vivamus egestas risus in magna varius commodo. Sed semper viverra egestas. Etiam pretium porttitor lectus, vel ornare neque porta volutpat.</p>
      <p class="copy">Vestibulum ante ipsum primis in faucibus orci luctus et ultrices posuere cubilia Curae; Ut et scelerisque ante. Donec erat purus, faucibus vitae congue vel, porttitor nec lectus. Aenean a nibh eget turpis vehicula tempus ac sed massa. Vestibulum dolor nulla, ultrices ac tincidunt sed, laoreet non est. Suspendisse lobortis turpis in odio blandit ac inter-dum lorem euismod. Etiam risus massa, vulputate eu pellentesque et, consectetur a neque.</p>
      <p class="copy">Lorem ipsum dolor sit amet, consect- etuer adipiscing elit, sed diam nonummy nibh euismod tincidunt ut laoreet dolore magna aliquam erat volutpat.</p>
      <div class="btn-blue">READ MORE</div>
    </section>

    <section class="box regions">
      <h2>REGIONS</h2>
      <div class="region-list">
        <div class="region"><h3>Mountain Pacific</h3><ul><li>Vancouver Island</li><li>Vancouver</li><li>Calgary</li></ul></div>
        <div class="region"><h3>Western</h3><ul><li>Edmonton</li><li>Saskatchewan</li><li>Winnipeg</li></ul></div>
        <div class="region central"><h3>Central</h3><ul><li>National Capital<br>Ottawa</li><li>Southwestern Ontario</li><li>Montreal</li><li>Toronto</li></ul></div>
        <div class="region atlantic"><h3>Atlantic</h3><ul><li>Nova Scotia</li><li>Terra-Nova, St. John's</li><li>Prince Edward Island</li><li>Atlantic, St. John's</li></ul></div>
      </div>
    </section>
  </main>

  <footer class="footer">
    <div class="footer-links">Home<span>/</span>About<span>/</span>Board<span>/</span>Chapters<span>/</span>Member Space<span>/</span>Resources &amp; Knowledge<span>/</span>Sponsorship<span>/</span>Exhibit<span>/</span>Member Login<span>/</span>Contact Us</div>
    <div class="copyright">Copyright 2013 by Kelvo .&nbsp; All Right Reserved&nbsp; /&nbsp; Privacy Policy</div>
  </footer>
</div>
</body>
</html>
```